Covid 19 Exit Strategy one page brochure

I would like to design, and will need URGENT help, a brochure detailing a Covid 19 Exit Strategy plan. This brochure will need to be understood easily and the graphics inside should make it easy for people to understand without reading the entire text. This project is quite urgent and needs to be completed THIS WEEK - by Saturday may 16th at the latest. I am attaching two examples. I will provide the text.

```html
<!DOCTYPE html>
<html lang="en">
<head>
<meta charset="utf-8">
<title>COVID-19 Phased Exit Strategy</title>
<link rel="stylesheet" href="https://fonts.googleapis.com/css2?family=Work+Sans:wght@600;700&family=Lato:wght@400;700&display=swap">
<style>
:root{
  --red:#e3211f;
  --red-dark:#c9191a;
  --blue:#45a6df;
  --white:#ffffff;
  --ink:#1a1a1a;
  --stage:#5b5a5b;
  --tick:#45a6df;
}
*{box-sizing:border-box;margin:0;padding:0}
html,body{width:1200px;height:1200px;overflow:hidden}
body{background:var(--stage);font-family:"Lato",sans-serif;position:relative}
.brochure{position:absolute;left:244px;top:0;width:712px;height:1200px;background:var(--white);overflow:hidden}
.title-main{position:absolute;left:0;right:0;top:24px;text-align:center;font-family:"Work Sans",sans-serif;font-weight:700;color:var(--red);font-size:41px;line-height:1}
.title-sub{position:absolute;left:0;right:0;top:76px;text-align:center;font-family:"Work Sans",sans-serif;font-weight:700;color:var(--ink);font-size:42px;line-height:1}
.author-band{position:absolute;left:0;right:0;top:126px;height:46px;background:var(--blue);color:var(--white);text-align:center;font-family:"Work Sans",sans-serif;font-weight:700;font-size:41px;line-height:46px}
.req-pill{position:absolute;left:203px;width:291px;top:172px;height:31px;background:var(--red);border-radius:0 0 18px 18px;color:var(--white);text-align:center;font-family:"Work Sans",sans-serif;font-weight:600;font-size:20px;line-height:31px}
.req-col{position:absolute;top:222px;list-style:none;font-size:12.4px;line-height:15.3px;color:var(--ink)}
.req-col.left{left:14px;width:340px}
.req-col.right{left:364px;width:340px;border-left:1px solid #333;padding-left:8px}
.req-col li{position:relative;padding-left:21px;margin-bottom:6px}
.req-col li svg{position:absolute;left:0;top:1px;width:15px;height:15px}
.plan{position:absolute;left:0;right:0;top:446px;height:673px;background:radial-gradient(circle at 70% 40%,#ef3a35,var(--red) 55%,var(--red-dark));color:var(--white)}
.plan-title{position:absolute;left:0;right:0;top:17px;text-align:center;font-family:"Work Sans",sans-serif;font-weight:700;font-size:21px}
.stage-band{position:absolute;left:0;right:0;top:50px;height:38px;background:var(--blue);display:flex;align-items:center}
.stage-label{font-family:"Work Sans",sans-serif;font-weight:700;font-size:20px;margin-left:35px;width:94px}
.stage-note{font-weight:700;font-size:12.3px;line-height:15px}
.sequence{position:absolute;left:0;right:0;top:93px;text-align:center;font-size:17.5px;font-weight:700;padding-left:60px}
.step{position:absolute;width:275px}
.step .badge{position:absolute;left:-52px;top:2px;width:46px;height:46px;border-radius:50%;background:var(--blue);border:2px solid var(--white)}
.step h3{font-family:"Work Sans",sans-serif;font-weight:700;font-size:16.5px;line-height:19px}
.step p{font-size:11.2px;line-height:13.8px;margin-top:1px}
.col-l{left:88px}
.col-r{left:417px}
.footer-line{position:absolute;left:0;right:0;top:1119px;height:12px;background:var(--white)}
.footer{position:absolute;left:0;right:0;top:1131px;height:69px;background:var(--blue);color:var(--white);text-align:center;font-family:"Work Sans",sans-serif;font-weight:600;font-size:19px;letter-spacing:3px;line-height:69px}
</style>
</head>
<body>
<main class="brochure">
  <h1 class="title-main">COVID-19</h1>
  <h2 class="title-sub">Phased Exit Strategy</h2>
  <div class="author-band">Developed by Lena Varga</div>
  <div class="req-pill">General Requirements</div>

  <svg width="0" height="0" style="position:absolute">
    <symbol id="tick" viewBox="0 0 16 16"><circle cx="8" cy="8" r="7" fill="none" stroke="#45a6df" stroke-width="1.2"/><path d="M4.5 8.2l2.3 2.3 4.7-4.8" fill="none" stroke="#45a6df" stroke-width="1.5"/></symbol>
  </svg>

  <ul class="req-col left">
    <li><svg><use href="#tick"/></svg>Single digit downward trend of documented cases within the past 14-days.</li>
    <li><svg><use href="#tick"/></svg>Hospitals and the health care system are capable of treating patients without operating on a crisis mode.</li>
    <li><svg><use href="#tick"/></svg>Ability to screen and test symptomatic individuals within 24 hours of identification. Increased and sufficient testing capacity, to test at least 50% of all population if necessary within a timeframe of 3 months.</li>
    <li><svg><use href="#tick"/></svg>Ability to surge ICU capacity on a short notice - 24h.</li>
    <li><svg><use href="#tick"/></svg>Ability to track and trace infected patients and contacts on a live basis and across the country and ability to react quickly to any unusual trends or outbreaks.</li>
  </ul>
  <ul class="req-col right">
    <li><svg><use href="#tick"/></svg>Plan in place to trigger targeted or full-scale containment in case of sudden outbreaks</li>
    <li><svg><use href="#tick"/></svg>Mandatory use of masks (at least surgical grade) for everyone in all public areas and at work. Mandatory use of N95, or equivalent, masks for all healthcare front workers and for all government agencies and authorities that are involved in overseeing the containment activities.</li>
    <li><svg><use href="#tick"/></svg>Mandatory daily checks of body temperature for everyone at the workplace or entering public areas.</li>
    <li><svg><use href="#tick"/></svg>Mandatory sanitation in all places - use of disinfection available on a large scale.</li>
  </ul>

  <section class="plan" role="img" aria-label="Red background with faint virus particle illustration">
    <h2 class="plan-title">Phased Covid-19 Lockdown Exit Strategy Plan</h2>
    <div class="stage-band">
      <span class="stage-label">Stage 1 :</span>
      <span class="stage-note">To enter this stage, additional to the general requirements, the Effective Reproduction<br>Number (Rt) must be less than 1 and the death rate at less than 3%.</span>
    </div>
    <p class="sequence">The economy and social activities can resume in this sequence :</p>

    <div class="step col-l" style="top:120px"><span class="badge" role="img" aria-label="Self-isolation icon"></span><h3>Self-Isolate</h3><p>Elderly (60+ years old) and vulnerable individuals should continue to self-isolate</p></div>
    <div class="step col-l" style="top:178px"><span class="badge" role="img" aria-label="Group of people icon"></span><h3>No Gathering</h3><p>No more than 10 people maximum gathering at a time in public areas and at work.</p></div>
    <div class="step col-l" style="top:240px"><span class="badge" role="img" aria-label="Person working at home icon"></span><h3>Work From Home</h3><p>If possible or for jobs that do not have to be necessarily in an office setup.</p></div>
    <div class="step col-l" style="top:300px"><span class="badge" role="img" aria-label="Two people apart icon"></span><h3>Social Distancing</h3><p>People should continue to wear masks and use disinfectants.</p></div>
    <div class="step col-l" style="top:367px"><span class="badge" role="img" aria-label="Travel ticket icon"></span><h3>Non-Essential Travel</h3><p>should be minimized between cities and regions</p></div>
    <div class="step col-l" style="top:420px"><span class="badge" role="img" aria-label="Grid blocks icon"></span><h3>Large Businesses</h3><p>300 people and more, manufacturing, services, etc. can reopen progressively. Common areas should remain closed (cafeteria, restaurant, gym, meeting rooms of no more than 5 people).</p></div>
    <div class="step col-l" style="top:511px"><span class="badge" role="img" aria-label="Hand pointer icon"></span><h3>Small Businesses</h3><p>300 people and less can reopen as well with the same conditions as large businesses.</p></div>
    <div class="step col-l" style="top:580px"><span class="badge" role="img" aria-label="Shop building icon"></span><h3>Commercial shops</h3><p>Commercial shops can reopen. Shops should control the flow of people in their facilities not to exceed 30% at a time of standard capacity.</p></div>

    <div class="step col-r" style="top:124px"><span class="badge" role="img" aria-label="Pills icon"></span><h3>Pharmacies Open</h3><p>they must make available disinfectant for use by clients and will continue to comply with social distancing.</p></div>
    <div class="step col-r" style="top:194px"><span class="badge" role="img" aria-label="Bus icon"></span><h3>Transportation</h3><p>buses, taxis, airlines will resume progressively. No air travels permitted in and out of Covid-19 known hotspots, locally or internationally.</p></div>
    <div class="step col-r" style="top:268px"><span class="badge" role="img" aria-label="Religious symbol icon"></span><h3>Religious Sites</h3><p>Religious sites can reopen with a maximum capacity of 30% or less. Social distancing and wearing masks is mandatory.</p></div>
    <div class="step col-r" style="top:343px"><span class="badge" role="img" aria-label="Hotel icon"></span><h3>Hotels &amp; Tourism</h3><p>can reopen but must operate at 30% or less capacity. All common areas (restaurants, gyms, swimming pools, conference rooms, etc.) should remain closed.</p></div>
    <div class="step col-r" style="top:420px"><span class="badge" role="img" aria-label="Plate and cutlery icon"></span><h3>Coffee &amp; Restaurants</h3><p>can reopen but must operate at 30% capacity as well and comply with social distancing. Clients must wear as much as possible their masks if they are not consuming food/coffee.</p></div>
    <div class="step col-r" style="top:511px"><span class="badge" role="img" aria-label="School building icon"></span><h3>All schools should remain closed</h3><p>On-line courses should continue be the preferred method for education.</p></div>
    <div class="step col-r" style="top:582px"><span class="badge" role="img" aria-label="Film strip icon"></span><h3>Large Scale Events</h3><p>cinema, theaters, sport, business conferences, etc.) should remain closed or operate virtually. Sport events can resume but without spectators.</p></div>
  </section>

  <div class="footer-line"></div>
  <footer class="footer">www.exitplanguide.org</footer>
</main>
</body>
</html>
```